Website Design for Chef Wirra Chinese Restaurant

Chef Wirra is a new Chinese Restaurant. It offers exceptional dining experience with authentic and dynamic dishes created with quality ingredients.

A vivid website theme is required to promote this new restaurant online. Logo, menu, wine list and a few other files are attached for help with designing.

A very rough demo website has been setup and can be accessed via http://www.chefwirra.com.au. It is for telling designers what content is shown up on each page (except for homepage). By reading the about us page, designers can get some more info of Chef Wirra. However, the layout, theme color, font, etc are not set in stone. Visitors should be able to feel Chef Wirra restaurant's authentic Chinese cuisine and high hygiene standard. Home page of the website could be The "Our website is coming soon" description is shown on demo site but do not required to be presented on new design.

Some main pages design should be included: Home (landing page), About us, Menu (Dishes), Winelist, Gallery, Contact us. No HTML and coding required. The output should be well layered psd or png files with acceptable resolution for web use.

A few other website can be referred to are:

http://kelpmerachinese.com.au/
http://www.stone-lamp.com/
http://brimvale.com.au/
http://harvelrestaurant.com.au/
http://www.tilmorerestaurant.com.au/
http://www.thequill.com.au/

Industry/Entity Type

Restaurant

Requirements
Nice to have
• I expect designs of at least these webpages: homepage, menu page and contact us page. If you can provide "about us" page as well, it will probably help you win the competition. well layered psd or png file is my preference.
Should not have
• You don't have to make html/cs/js or any coding. All I need is just art design

```html
<!DOCTYPE html>
<html lang="en">
<head>
<meta charset="utf-8">
<title>Chef Wirra Chinese Restaurant – Yum Cha Menu</title>
<link href="https://fonts.googleapis.com/css2?family=Arimo:wght@400;700&display=swap" rel="stylesheet">
<style>
  :root{
    --red:#e3262b;
    --red-dark:#c81a1f;
    --cream:#fffccc;
    --cream-text:#fff6c8;
    --ink:#333333;
    --body-ink:#3a3a3a;
    --footer:#1b1b1b;
    --nav-band:#d9d4cf;
    --white:#ffffff;
  }
  *{box-sizing:border-box;margin:0;padding:0}
  html,body{width:1200px;height:1060px;overflow:hidden;background:var(--white)}
  body{position:relative;font-family:"Arimo",Arial,sans-serif;color:var(--ink)}
  .abs{position:absolute}

  /* top bar */
  .top-bar{left:0;top:0;width:1200px;height:54px;background:var(--red);border-bottom:2px solid #5a1a1a}
  .reservation{left:88px;top:14px;display:flex;align-items:center;gap:8px;color:var(--white);font-weight:700;font-size:16px}
  .social{right:112px;top:6px;display:flex;gap:10px}
  .social span{width:42px;height:42px;border-radius:50%;background:var(--white);display:flex;align-items:center;justify-content:center}
  .social .dot{width:16px;height:16px;background:var(--red);border-radius:3px}

  /* brand band */
  .brand-band{left:0;top:54px;width:1200px;height:126px;background:var(--cream);border-bottom:2px solid #333}
  .flourish{top:64px;width:234px;height:104px;background:linear-gradient(90deg,rgba(232,80,20,.15),rgba(232,80,20,.35),rgba(232,80,20,.15));border-radius:50px}
  .flourish.left{left:178px}
  .flourish.right{left:744px}
  .logo-arch{left:459px;top:8px;width:240px;height:172px;background:var(--cream);border-radius:120px 120px 0 0;border-top:5px solid #f4c9a8}
  .logo{left:459px;top:40px;width:240px;text-align:center}
  .logo .mark{width:34px;height:34px;background:var(--red);margin:0 auto 14px}
  .logo .name{font-weight:700;font-size:22px;color:var(--red)}
  .logo .sub{font-weight:700;font-size:10px;color:#222;margin-top:8px;letter-spacing:.2px}

  /* main nav */
  .main-nav{left:0;top:182px;width:1200px;height:51px;background:linear-gradient(90deg,#e8e2dc,var(--nav-band),#cfc8c2,#e1dbd5)}
  .main-nav ul{list-style:none;position:absolute;top:12px;left:0;width:1200px}
  .main-nav li{position:absolute;font-size:20px;color:var(--red)}
  .main-nav li.current{color:#111}

  /* sidebar */
  .menu-sidebar{left:77px;top:254px;width:313px;height:606px;background:var(--red);border:1px solid var(--red-dark)}
  .menu-sidebar h2{position:absolute;left:0;top:6px;width:100%;text-align:center;font-weight:400;font-size:26px;line-height:28px;color:var(--cream-text)}
  .sidebar-divider{left:14px;top:35px}
  .menu-sidebar ul{list-style:none;position:absolute;left:16px;top:68px}
  .menu-sidebar li{font-weight:700;font-size:15px;line-height:26px;color:var(--cream-text)}
  .sidebar-ornament{left:56px;top:548px;width:164px;height:46px;background:linear-gradient(180deg,rgba(255,246,200,.2),rgba(255,246,200,.55));border-radius:40px 40px 6px 6px}

  /* content */
  .section-title{left:409px;top:254px;width:636px;text-align:center;font-weight:400;font-size:28px;color:var(--ink)}
  .intro{left:409px;top:337px;width:482px;font-size:14px;line-height:22.5px;color:var(--body-ink)}
  .dish-list{list-style:none;top:446px;width:214px}
  .dish-list li{font-weight:700;font-size:15px;line-height:26px;color:var(--red)}
  .dish-list.col-a{left:408px}
  .dish-list.col-b{left:660px}
  .dish-photo{left:928px;width:160px;border-radius:50%;background:radial-gradient(circle at 50% 40%,#f3dcc4,#d9a766 60%,#b57a3a)}

  /* footer */
  .site-footer{left:0;top:946px;width:1200px;height:114px;background:var(--footer)}
  .site-footer ul{list-style:none}
  .site-footer li{position:absolute;top:26px;font-size:16px;color:var(--cream-text)}
  .site-footer li.current{color:var(--red)}
  .copyright{position:absolute;top:66px;left:0;width:1200px;text-align:center;font-size:14px;color:var(--cream-text)}
  .copyright b{color:var(--red);font-weight:400}
</style>
</head>
<body>

<header>
  <div class="abs top-bar"></div>
  <div class="abs reservation">
    <svg width="22" height="22" viewBox="0 0 24 24"><path fill="#fff" d="M6.6 10.8a15.1 15.1 0 0 0 6.6 6.6l2.2-2.2c.3-.3.7-.4 1-.2 1.1.4 2.3.6 3.6.6.6 0 1 .4 1 1V20c0 .6-.4 1-1 1A17 17 0 0 1 3 4c0-.6.4-1 1-1h3.5c.6 0 1 .4 1 1 0 1.3.2 2.5.6 3.6.1.3 0 .7-.2 1z"/></svg>
    Make a Reservation : +44 155 010 2847
  </div>
  <div class="abs social" aria-label="Social links">
    <span aria-label="Social profile"><i class="dot"></i></span>
    <span aria-label="Social profile"><i class="dot"></i></span>
    <span aria-label="Social profile"><i class="dot"></i></span>
    <span aria-label="Social profile"><i class="dot"></i></span>
    <span aria-label="Email">
      <svg width="20" height="15" viewBox="0 0 20 15"><rect width="20" height="15" rx="2" fill="#e3262b"/><path d="M1 2l9 6 9-6" stroke="#fff" stroke-width="1.8" fill="none"/></svg>
    </span>
  </div>

  <div class="abs brand-band"></div>
  <div class="abs flourish left" role="img" aria-label="Orange floral scroll ornament"></div>
  <div class="abs flourish right" role="img" aria-label="Orange floral scroll ornament"></div>
  <div class="abs logo-arch"></div>
  <div class="abs logo">
    <div class="mark"></div>
    <div class="name">Chef Wirra</div>
    <div class="sub">CHEF WIRRA CHINESE RESTAURANT</div>
  </div>

  <nav class="abs main-nav">
    <ul>
      <li style="left:211px">Home</li>
      <li style="left:316px">About</li>
      <li class="current" style="left:427px">Menu</li>
      <li style="left:529px">Winelist</li>
      <li style="left:658px">Facilities</li>
      <li style="left:794px">Gallery</li>
      <li style="left:911px">Contact</li>
    </ul>
  </nav>
</header>

<aside class="abs menu-sidebar">
  <h2>Menu</h2>
  <svg class="abs sidebar-divider" width="284" height="44" viewBox="0 0 284 44">
    <g stroke="#fff6c8" stroke-width="1.2"><line x1="0" y1="20" x2="104" y2="20"/><line x1="14" y1="24" x2="104" y2="24"/><line x1="180" y1="20" x2="284" y2="20"/><line x1="180" y1="24" x2="270" y2="24"/></g>
    <circle cx="142" cy="22" r="22" fill="#fff6c8"/>
    <g fill="#e3262b"><rect x="133" y="10" width="2.2" height="10"/><rect x="137" y="10" width="2.2" height="10"/><rect x="141" y="10" width="2.2" height="10"/><rect x="135" y="18" width="6" height="17" rx="2"/><path d="M148 10c4 2 5 8 3 13h-2v12h-4V12c0-1.5 1.5-2.5 3-2z"/></g>
  </svg>
  <ul>
    <li>Yum Cha</li><li>Entrée</li><li>Soup</li><li>Cold Dishes</li><li>Seafood Dishes</li><li>Steak Dishes</li><li>Chicken Dishes</li><li>Duck Dishes</li><li>Lamb Dishes</li><li>Pork Dishes</li><li>Tofu Dishes</li><li>Hot Pot Dishes</li><li>Vegetable Dishes</li><li>Special flavour selections</li><li>Abalone and Sea Cucumber</li><li>Rice and Noodles</li><li>Dessert</li>
  </ul>
  <div class="abs sidebar-ornament" role="img" aria-label="Cream scroll ornament"></div>
</aside>

<main>
  <h1 class="abs section-title">Yum Cha</h1>
  <svg class="abs" style="left:411px;top:288px" width="634" height="48" viewBox="0 0 634 48">
    <g stroke="#e3262b" stroke-width="1.4"><line x1="0" y1="22" x2="284" y2="22"/><line x1="14" y1="27" x2="284" y2="27"/><line x1="350" y1="22" x2="634" y2="22"/><line x1="350" y1="27" x2="620" y2="27"/></g>
    <circle cx="317" cy="24" r="23" fill="#e3262b"/>
    <path d="M307 22a6 6 0 0 1 4-10 7 7 0 0 1 12 0 6 6 0 0 1 4 10v9h-20z" fill="none" stroke="#fff" stroke-width="2.2"/>
    <line x1="307" y1="27" x2="327" y2="27" stroke="#fff" stroke-width="2"/>
  </svg>

  <p class="abs intro">also known as ban ming, is a southern Chinese style morning or afternoon tea, which involves drinking Chinese tea and eating dim sum small dishes (steamed, fried or bakes sweets). In specialist restaurants, staff will commonly wheel around heated trolleys serving small yum cha dishes.</p>

  <ul class="abs dish-list col-a">
    <li>Prawn Dumplings</li><li>Scallop Dumplings</li><li>Vegetarian Dumplings</li><li>Minced Pork &amp; Peanut Dumplings</li><li>Steamed Custerd Bun with Egg Yolk</li><li>Spicy Chicken Feet in Black bean Sauce</li><li>Steamed Pork Ribs</li><li>Spicy Ox Tripe</li><li>Malay Cakes</li><li>Shanghai Pork Buns</li><li>Steamed Beef Balls</li><li>Pan Fried Water Chestnuts Cakes</li>
  </ul>
  <ul class="abs dish-list col-b">
    <li>Spicy Chicken Feet in Black bean Sauce</li><li>Steamed pork Ribs</li><li>Spicy Ox Tripe</li><li>Malay Cakes</li><li>Shanghai Pork Buns</li><li>Steamed Beef Balls</li><li>Pan Fried Water Chestnuts Cakes</li><li>Prawn Dumplings</li><li>Scallop Dumplings</li><li>Vegetarian Dumplings</li><li>Minced Pork &amp; Peanut Dumplings</li><li>Steamed Custard Bun with Egg Yolk</li>
  </ul>

  <div class="abs dish-photo" style="top:330px;height:148px" role="img" aria-label="Prawn dumplings in a bamboo steamer"></div>
  <div class="abs dish-photo" style="left:910px;top:482px;width:190px;height:118px;background:radial-gradient(ellipse at 50% 50%,#e8ead2,#f4f4f0 70%,#ffffff)" role="img" aria-label="Pan fried dumplings on a white plate"></div>
  <div class="abs dish-photo" style="top:630px;height:132px" role="img" aria-label="Steamed custard buns in a bamboo steamer"></div>
  <div class="abs dish-photo" style="top:770px;height:138px;background:radial-gradient(circle at 50% 45%,#e0452e,#c9542e 45%,#d9a766 65%,#b57a3a)" role="img" aria-label="Spicy chicken feet in a bamboo steamer"></div>
</main>

<footer class="abs site-footer">
  <ul>
    <li class="current" style="left:218px">Home</li>
    <li style="left:317px">About</li>
    <li style="left:428px">Menu</li>
    <li style="left:530px">Winelist</li>
    <li style="left:659px">Facilities</li>
    <li style="left:796px">Events</li>
    <li style="left:912px">Contact</li>
  </ul>
  <p class="copyright">© <b>Chef Wirra</b> - 2014. All Rights Reserved.</p>
</footer>

</body>
</html>
```